Marlo's Bakes Tortehouse LLC website

Artisan cheesecake business looking for excellent talent to design bright, fun, engaging website for our company. We also recently acquired a food truck so we are able to cater and attend food truck events.
Our mission is to create fun, unique, delicious flavors of cheesecake and we bake them in mason jars and whole cheesecakes. We strive to exceed our customers' expectations in everything we do.
Target Market(s)
Foodies, cheesecake lovers, dessert lovers, food truck people,
Industry/Entity Type
Dessert, Catering, Pop Up events, Food truck
Coding
Coded - Design and coding required
Number of Pages Required
4 page
Requirements
Must have
- Pictures of my cheesecakes
Nice to have
- Bright, colorful, eye-catching design with a good flow

```html
<!DOCTYPE html>
<html lang="en">
<head>
<meta charset="utf-8">
<title>Marlo's Bakes Tortehouse LLC</title>
<link href="https://fonts.googleapis.com/css2?family=Anton&family=Montserrat:wght@500;600;700&family=Playball&family=Tinos:ital,wght@0,400;0,700;1,400;1,700&display=swap" rel="stylesheet">
<style>
:root{
  --pink:#f6c6cb;
  --pink-deep:#e3a0a8;
  --rose:#e0909b;
  --brown:#5d463b;
  --brown-dark:#4a362e;
  --ink:#2b2220;
  --grey:#e5e4e2;
  --white:#ffffff;
}
*{margin:0;padding:0;box-sizing:border-box}
html,body{width:1200px;height:4922px;overflow:hidden}
body{position:relative;background:var(--white);font-family:"Tinos",serif;color:var(--ink)}
.abs{position:absolute}
.script{font-family:"Playball",cursive}
.btn{position:absolute;width:153px;height:36px;border-radius:18px;font-family:"Montserrat",sans-serif;font-weight:600;font-size:18px;display:flex;align-items:center;justify-content:center}
.btn-brown{background:var(--brown);color:var(--white)}
.btn-pink{background:var(--pink-deep);color:var(--brown-dark)}
.section-title{position:absolute;left:0;width:1200px;text-align:center;font-family:"Playball",cursive;font-size:44px;color:var(--brown)}
.section-title::after{content:"";display:block;width:60px;height:2px;background:var(--rose);margin:4px auto 0}

/* header */
.top-strip{position:absolute;top:0;left:0;width:1200px;height:7px;background:var(--pink)}
.header{position:absolute;top:7px;left:0;width:1200px;height:138px;background:var(--white);border-bottom:1px solid #eee}
.logo{position:absolute;left:99px;top:27px;width:96px;height:96px;border-radius:50%;background:var(--pink);display:flex;align-items:center;justify-content:center;text-align:center;font-family:"Tinos",serif;font-size:15px;color:var(--white);line-height:1.1}
.topinfo{position:absolute;top:26px;font-size:14px;color:var(--ink);line-height:1.3}
.topinfo .lead{color:var(--rose);text-decoration:underline}
.follow{position:absolute;left:1026px;top:24px;font-size:12px;color:var(--rose)}
.follow span{display:inline-block;width:11px;height:11px;background:var(--rose);margin-right:3px;margin-top:4px}
.nav{position:absolute;top:101px;font-family:"Tinos",serif;font-size:14px;letter-spacing:.5px;color:var(--ink)}
.nav.active{border-bottom:1px solid var(--ink)}

/* hero */
.hero{position:absolute;top:145px;left:0;width:1200px;height:652px;background:var(--grey)}
.hero-photo{position:absolute;left:535px;top:0;width:665px;height:652px;background:radial-gradient(ellipse at 55% 55%,#f4ecd8 0%,#e8dcbe 35%,#b89a6e 60%,#d9d6d2 85%)}
.hero-kicker{position:absolute;left:102px;top:155px;font-family:"Playball",cursive;font-size:54px;color:var(--brown)}
.hero-big{position:absolute;left:99px;font-family:"Anton",sans-serif;color:var(--rose);line-height:1}
.hero-big.one{top:213px;font-size:116px}
.hero-big.two{top:325px;font-size:64px}

/* about */
.about{position:absolute;top:797px;left:0;width:1200px;height:562px;background:var(--pink)}
.about-photo{position:absolute;left:103px;top:151px;width:409px;height:331px;border-radius:16px;background:linear-gradient(180deg,#b9cde6 0%,#e7a3bd 45%,#d98aa8 70%,#8a9a72 100%)}
.about-text{position:absolute;left:564px;top:170px;width:525px;font-size:12.6px;line-height:1.32;text-align:justify;color:var(--ink)}
.about-text p+p{margin-top:14px}

/* events */
.event{position:absolute;width:330px;height:140px}
.event svg{position:absolute;left:0;top:0}
.event .day{position:absolute;left:0;top:42px;width:92px;text-align:center;font-family:"Playball",cursive;font-size:15px;line-height:1.05;color:var(--brown-dark)}
.event .day b{font-family:"Tinos",serif;font-size:16px;display:block}
.event h3{position:absolute;left:108px;top:0;font-family:"Tinos",serif;font-weight:400;font-size:21px;line-height:1.08;color:var(--rose)}
.event p{position:absolute;left:108px;top:52px;font-size:12.5px;line-height:1.25;color:#444}
.event a{position:absolute;left:108px;top:90px;font-size:17px;font-style:italic;font-weight:700;color:var(--brown);text-decoration:underline}
.dots{position:absolute;top:1916px;left:577px;display:flex;gap:8px}
.dots span{width:11px;height:11px;border-radius:50%;border:1px solid var(--brown)}
.dots span.on{background:var(--brown-dark)}

/* small batch */
.batch{position:absolute;top:1993px;left:0;width:1200px;height:711px;background:var(--brown)}
.batch .title{position:absolute;top:58px;width:1200px;text-align:center;font-family:"Playball",cursive;font-size:44px;color:var(--pink-deep)}
.round{position:absolute;top:189px;width:306px;height:306px;border-radius:50%;border:4px solid var(--pink-deep);padding:8px}
.round div{width:100%;height:100%;border-radius:50%}
.round-label{position:absolute;top:521px;width:306px;text-align:center;font-size:14px;font-weight:700;color:var(--white);letter-spacing:.5px}

/* artisan */
.card{position:absolute;top:2937px;width:294px;height:293px;box-shadow:0 3px 8px rgba(0,0,0,.25)}
.card .img{width:100%;height:254px}
.card .label{height:39px;background:var(--pink-deep);display:flex;align-items:center;justify-content:center;font-size:16px;letter-spacing:1px;color:var(--brown-dark)}

/* menu */
.menu{position:absolute;top:3354px;left:0;width:1200px;height:537px;background:radial-gradient(circle at 30% 30%,#a8474a 0%,#7a2a2d 40%,#4a2421 75%),#5a2a28}
.menu::after{content:"";position:absolute;inset:0;background:rgba(60,40,35,.35)}
.price-card{position:absolute;top:90px;width:237px;height:384px;background:var(--white);z-index:1}
.price-card .head{padding:40px 0 0 38px;height:149px}
.price-card.feature .head{background:var(--pink-deep)}
.price-card .plan{font-size:13px;font-weight:700;letter-spacing:.5px}
.price-card .amt{font-size:31px;font-weight:700;margin-top:10px}
.price-card .sub{font-size:12px;margin-top:6px}
.price-card .body{padding:10px 0 0 38px;font-size:12.5px;line-height:1.5}
.price-card .mini{position:absolute;left:25px;top:330px;width:117px;height:24px;border-radius:12px;background:var(--brown);color:var(--white);font-family:"Montserrat",sans-serif;font-size:13px;font-weight:600;display:flex;align-items:center;justify-content:center}
.menu-title{position:absolute;left:831px;top:148px;font-family:"Playball",cursive;font-size:44px;color:var(--white);z-index:1}
.menu-title::after{content:"";display:block;width:60px;height:2px;background:var(--pink-deep);margin:2px 0 0 14px}
.menu-text{position:absolute;left:655px;top:235px;width:450px;font-size:13px;line-height:1.3;color:var(--white);text-align:center;z-index:1}

/* orders */
.orders-sub{position:absolute;top:4017px;left:160px;width:880px;text-align:center;font-size:11.5px;font-style:italic;line-height:1.3;color:#444}
.order-col{position:absolute;top:4090px;width:440px}
.order-col h3{font-family:"Playball",cursive;font-weight:400;font-size:38px;color:var(--rose);text-decoration:underline;text-decoration-thickness:1px;text-underline-offset:5px;margin-bottom:14px}
.order-item{margin-bottom:14px}
.order-item b{display:block;font-size:26px;line-height:1.1}
.order-item i{display:block;font-size:15px;color:#444}
.divider{position:absolute;left:585px;top:4097px;width:1px;height:296px;background:#ccc}

/* footer */
.footer{position:absolute;top:4458px;left:0;width:1200px;height:464px;background:var(--brown)}
.footer-logo{position:absolute;left:172px;top:54px;width:168px;height:168px;border-radius:50%;background:var(--pink);display:flex;align-items:center;justify-content:center;text-align:center;font-size:24px;color:var(--white);line-height:1.1}
.footer-about{position:absolute;left:99px;top:232px;width:330px;text-align:center;font-size:13.5px;line-height:1.45;color:var(--white)}
.vline{position:absolute;width:2px;background:var(--white)}
.footer h4{position:absolute;top:70px;font-family:"Montserrat",sans-serif;font-weight:600;font-size:21px;color:var(--pink-deep)}
.qlink{position:absolute;left:514px;font-size:14px;color:var(--white)}
.qlink::before{content:"›";position:absolute;left:-18px;top:-2px;font-size:16px}
.contact{position:absolute;left:904px;font-size:17px;color:var(--white)}
.copyright{position:absolute;top:4865px;left:0;width:1200px;height:57px;background:var(--pink);border-top:3px solid var(--white);display:flex;align-items:center;justify-content:center;font-family:"Montserrat",sans-serif;font-size:11px;color:var(--brown-dark)}
</style>
</head>
<body>

<div class="top-strip"></div>
<header class="header">
  <div class="logo">Marlo's<br>Bakes</div>
  <div class="topinfo" style="left:514px">
    <svg width="12" height="12" viewBox="0 0 24 24"><path d="M6 2l4 4-2 3c1 3 4 6 7 7l3-2 4 4-3 4C10 22 2 14 2 5z" fill="none" stroke="#e0909b" stroke-width="2"/></svg>
    <span class="lead">Order Now 555-201-4477</span><br><span style="margin-left:15px">Local pick up only</span>
  </div>
  <div class="topinfo" style="left:768px">
    <svg width="13" height="10" viewBox="0 0 26 20"><rect x="1" y="1" width="24" height="18" fill="none" stroke="#e0909b" stroke-width="2"/><path d="M1 1l12 10L25 1" fill="none" stroke="#e0909b" stroke-width="2"/></svg>
    <span class="lead">Contact Email</span><br><span style="margin-left:19px">hello@marlosbakes.test</span>
  </div>
  <div class="follow">Follow Us<br><span></span><span></span><span></span><span></span></div>
  <div class="nav active" style="left:502px">HOME</div>
  <div class="nav" style="left:592px">MENU</div>
  <div class="nav" style="left:682px">EVENTS</div>
  <div class="nav" style="left:787px">ORDER</div>
  <div class="nav" style="left:890px">ABOUT US</div>
  <div class="nav" style="left:1009px">CONTACT US</div>
</header>

<section class="hero">
  <div class="hero-photo" role="img" aria-label="Slice of coconut cream cheesecake with whipped cream rosettes on a graham crust"></div>
  <div class="hero-kicker">Cheesecake is</div>
  <div class="hero-big one">A love</div>
  <div class="hero-big two">Like no other.</div>
  <div class="btn btn-brown" style="left:99px;top:421px">Order Now</div>
</section>

<section class="about">
  <div class="section-title" style="top:50px">About Us</div>
  <div class="about-photo" role="img" aria-label="The owners standing in front of the pink cheesecake food truck"></div>
  <div class="about-text">
    <p>consectetur adipiscing elit. Quid autem habent admirationis, cum prope accesseris? An hoc usque quaque, aliter in vita? Non igitur de improbo, sed de callido improbo quaerimus, qualis Q. Nam quibus rebus efficiuntur voluptates, eae non sunt in potestate sapientis. Negare non possum. Huic mori optimum esse propter desperationem sapientiae, illi propter spem vivere. Quid enim me prohiberet Epicureum esse, si probarem, quae ille diceret? . <b>Admirationis, cum prope accesseris? An hoc usque quaque, aliter in vita? Non igitur de improbo, sed de callido improbo quaerimus, qualis Q. Nam quibus rebus efficiuntur voluptates, eae non sunt</b> Huic mori optimum esse propter desperationem sapientiae, illi propter spem vivere. Quid enim me prohiberet Epicureum esse, si probarem, quae ille diceret? Qui-vere falsone, quaerere mittimus-dicitur oculis se privasse;</p>
    <p>potestate sapientis. Negare non possum. Huic mori optimum esse propter desperationem sapientiae, illi propter spem vivere. Quid enim me prohiberet Epicureum esse, si probarem, quae ille diceret? Qui-vere falsone, quaerere mittimus-dicitur oculis se privasse;</p>
  </div>
  <div class="btn btn-brown" style="left:564px;top:428px">Learn More</div>
</section>

<section class="events">
  <div class="section-title" style="top:1404px">Events</div>

  <div class="event" style="left:99px;top:1529px">
    <svg width="92" height="92" viewBox="0 0 92 92"><rect x="2" y="10" width="88" height="80" rx="8" fill="#5d463b"/><rect x="10" y="30" width="72" height="52" fill="#f6c6cb"/><rect x="18" y="0" width="10" height="22" rx="5" fill="#e0909b"/><rect x="64" y="0" width="10" height="22" rx="5" fill="#e0909b"/></svg>
    <div class="day">Monday<b>7/4</b></div>
    <h3>EFFICI NTUR VOLUP<br>DESPERATIONEM</h3>
    <p>Magnum cognitione dignumam<br>Averuntlectulis plerumque moriun</p>
    <a>Read More</a>
  </div>
  <div class="event" style="left:447px;top:1529px">
    <svg width="92" height="92" viewBox="0 0 92 92"><rect x="2" y="10" width="88" height="80" rx="8" fill="#5d463b"/><rect x="10" y="30" width="72" height="52" fill="#f6c6cb"/><rect x="18" y="0" width="10" height="22" rx="5" fill="#e0909b"/><rect x="64" y="0" width="10" height="22" rx="5" fill="#e0909b"/></svg>
    <div class="day">Tuesday<b>16/2</b></div>
    <h3>EFFICI NTUR VOLUP<br>DESPERATIONEM</h3>
    <p>Magnum cognitione dignumam<br>Averuntlectulis plerumque moriun</p>
    <a>Read More</a>
  </div>
  <div class="event" style="left:797px;top:1529px">
    <svg width="92" height="92" viewBox="0 0 92 92"><rect x="2" y="10" width="88" height="80" rx="8" fill="#5d463b"/><rect x="10" y="30" width="72" height="52" fill="#f6c6cb"/><rect x="18" y="0" width="10" height="22" rx="5" fill="#e0909b"/><rect x="64" y="0" width="10" height="22" rx="5" fill="#e0909b"/></svg>
    <div class="day">Friday<b>8/5</b></div>
    <h3>EFFICI NTUR VOLUP<br>DESPERATIONEM</h3>
    <p>Magnum cognitione dignumam<br>Averuntlectulis plerumque moriun</p>
    <a>Read More</a>
  </div>
  <div class="event" style="left:99px;top:1722px">
    <svg width="92" height="92" viewBox="0 0 92 92"><rect x="2" y="10" width="88" height="80" rx="8" fill="#5d463b"/><rect x="10" y="30" width="72" height="52" fill="#f6c6cb"/><rect x="18" y="0" width="10" height="22" rx="5" fill="#e0909b"/><rect x="64" y="0" width="10" height="22" rx="5" fill="#e0909b"/></svg>
    <div class="day">Thursday<b>29/4</b></div>
    <h3>EFFICI NTUR VOLUP<br>DESPERATIONEM</h3>
    <p>Magnum cognitione dignumam<br>Averuntlectulis plerumque moriun</p>
    <a>Read More</a>
  </div>
  <div class="event" style="left:447px;top:1722px">
    <svg width="92" height="92" viewBox="0 0 92 92"><rect x="2" y="10" width="88" height="80" rx="8" fill="#5d463b"/><rect x="10" y="30" width="72" height="52" fill="#f6c6cb"/><rect x="18" y="0" width="10" height="22" rx="5" fill="#e0909b"/><rect x="64" y="0" width="10" height="22" rx="5" fill="#e0909b"/></svg>
    <div class="day">Starday<b>10/4</b></div>
    <h3>EFFICI NTUR VOLUP<br>DESPERATIONEM</h3>
    <p>Magnum cognitione dignumam<br>Averuntlectulis plerumque moriun</p>
    <a>Read More</a>
  </div>
  <div class="event" style="left:797px;top:1722px">
    <svg width="92" height="92" viewBox="0 0 92 92"><rect x="2" y="10" width="88" height="80" rx="8" fill="#5d463b"/><rect x="10" y="30" width="72" height="52" fill="#f6c6cb"/><rect x="18" y="0" width="10" height="22" rx="5" fill="#e0909b"/><rect x="64" y="0" width="10" height="22" rx="5" fill="#e0909b"/></svg>
    <div class="day">Sunday<b>25/4</b></div>
    <h3>EFFICI NTUR VOLUP<br>DESPERATIONEM</h3>
    <p>Magnum cognitione dignumam<br>Averuntlectulis plerumque moriun</p>
    <a>Read More</a>
  </div>
  <div class="dots"><span class="on"></span><span></span><span></span></div>
</section>

<section class="batch">
  <div class="title">Small Batch Cheese cakes</div>
  <div class="round" style="left:99px"><div role="img" aria-label="Strawberry cheesecakes in mason jars" style="background:radial-gradient(circle,#f3e6d6 0%,#c9453f 55%,#3a1a16 100%)"></div></div>
  <div class="round" style="left:445px"><div role="img" aria-label="Slice of lemon cake with yellow frosting" style="background:radial-gradient(circle,#f7dd7a 0%,#e9c94f 55%,#2a2422 100%)"></div></div>
  <div class="round" style="left:793px"><div role="img" aria-label="Chocolate cake topped with raspberries" style="background:radial-gradient(circle,#7a3b24 0%,#4d2414 55%,#1a1010 100%)"></div></div>
  <div class="round-label" style="left:99px">LAELIUS CLAMORES</div>
  <div class="round-label" style="left:445px">TURPIUS PROPTER</div>
  <div class="round-label" style="left:793px">DEMOCRITEUM</div>
  <div class="btn btn-pink" style="left:520px;top:610px">More Cake</div>
</section>

<section class="artisan">
  <div class="section-title" style="top:2796px">Artisan Cheesecakes</div>
  <svg class="abs" style="left:48px;top:3015px" width="28" height="70" viewBox="0 0 28 70"><path d="M26 2L3 35l23 33" fill="none" stroke="#2b2220" stroke-width="3"/></svg>
  <svg class="abs" style="left:1128px;top:3015px" width="28" height="70" viewBox="0 0 28 70"><path d="M2 2l23 33L2 68" fill="none" stroke="#2b2220" stroke-width="3"/></svg>
  <div class="card" style="left:99px"><div class="img" role="img" aria-label="Whole cheesecake topped with sliced strawberries" style="background:radial-gradient(circle,#e24a3e 0%,#d43a30 45%,#ffffff 72%)"></div><div class="label">TURPIUS PROPTER</div></div>
  <div class="card" style="left:455px"><div class="img" role="img" aria-label="Heart-shaped chocolate cheesecake" style="background:radial-gradient(circle,#3b2219 0%,#2a1610 45%,#b9b9b9 75%)"></div><div class="label">DEMOCRITEUM</div></div>
  <div class="card" style="left:805px"><div class="img" role="img" aria-label="Chocolate cheesecake decorated for autumn" style="background:radial-gradient(circle,#6b3a22 0%,#4a2616 50%,#8a8a86 85%)"></div><div class="label">LAELIUS CLAMORES</div></div>
</section>

<section class="menu" role="img" aria-label="Background of strawberries and cheesecake">
  <div class="price-card" style="left:99px">
    <div class="head"><div class="plan">PHYSICS</div><div class="amt">$ 49.99</div><div class="sub">Paulum cum</div></div>
    <div class="body">Summum a vobis bonum<br>Quod, inquit, quamquam<br>Non enim ipsa genuit homi<br>Ergo illi intellegunt quid<br>Nec hoc ille non vidit, sed<br>In eo enim positum est id,</div>
    <div class="mini">Read More</div>
  </div>
  <div class="price-card feature" style="left:361px">
    <div class="head"><div class="plan">BEATUS</div><div class="amt">$ 49.99</div><div class="sub">Paulum cum</div></div>
    <div class="body">Summum a vobis bonum<br>Quod, inquit, quamquam<br>Non enim ipsa genuit homi<br>Ergo illi intellegunt quid<br>Nec hoc ille non vidit, sed<br>In eo enim positum est id,</div>
    <div class="mini">Read More</div>
  </div>
  <div class="menu-title">Menu</div>
  <div class="menu-text">Verum tamen cum de rebus grandioribus dicas, ipsae res verba rapiunt; Hoc non est positum in nostra actione. Quod ea non occurrentia fingunt, vincunt Aristonem; Haec para/doca illi, nos admirabilia dicamus. Et quidem, inquit, vehementer errat; Quarum ambarum rerum cum medicinam pollicetur, luxuriae licentiam pollicetur. Laelius clamores sofòw ille so lebat Edere compellans gumias ex ordine nostros.</div>
  <div class="btn btn-pink" style="left:803px;top:365px;z-index:1">Book A Table</div>
</section>

<section class="orders">
  <div class="section-title" style="top:3935px">Orders</div>
  <div class="orders-sub">Honestius nec turpi turpius. Tria genera bonorum Ruid iudicant sensus Suae qui nihil umquam magnumhonestius nec turpi turpiusbonorumiudicant onestius nec<br>Verum tamen cum de rebus grandioribus dicas, ipsae res verba rapiunt; Hoc non est positum in nostra actione. Quod ea non occurrentia</div>
  <div class="divider"></div>
  <div class="order-col" style="left:105px">
    <h3>Ordering Process</h3>
    <div class="order-item"><b>Respondeat totidem ,$18</b><i>PotestConsequens voluptatibus quibusdam voluptatibus</i></div>
    <div class="order-item" style="margin-top:26px"><b>Nodeatespo totidem ,$56</b><i>PotestConsequens voluptatibus quibusdam voluptatibus</i></div>
    <div class="order-item"><b>Pondeat totidem ,$78</b><i>PotestConsequens voluptatibus quibusdam voluptatibus</i></div>
    <div class="order-item"><b>Sepondeat totidem ,$21</b><i>PotestConsequens voluptatibus quibusdam voluptatibus</i></div>
  </div>
  <div class="order-col" style="left:728px">
    <h3>Payment Options</h3>
    <div class="order-item"><b>Respondeat totidem ,$18</b><i>PotestConsequens voluptatibus quibusdam voluptatibus</i></div>
    <div class="order-item" style="margin-top:26px"><b>Nodeatespo totidem ,$56</b><i>PotestConsequens voluptatibus quibusdam voluptatibus</i></div>
    <div class="order-item"><b>Pondeat totidem ,$78</b><i>PotestConsequens voluptatibus quibusdam voluptatibus</i></div>
    <div class="order-item"><b>Sepondeat totidem ,$21</b><i>PotestConsequens voluptatibus quibusdam voluptatibus</i></div>
  </div>
</section>

<footer class="footer">
  <div class="footer-logo">Marlo's<br>Bakes</div>
  <div class="footer-about">Lorem ipsum dolor sit amet, consectetur adipiscing elit. Quid autem habent admirationis, cum prope accesseris? An hoc usque quaque, aliter</div>
  <div class="vline" style="left:461px;top:100px;height:240px"></div>
  <div class="vline" style="left:759px;top:100px;height:240px"></div>
  <h4 style="left:493px">Quick Links</h4>
  <div class="qlink" style="top:146px">Home</div>
  <div class="qlink" style="top:183px">Menu</div>
  <div class="qlink" style="top:220px">Events</div>
  <div class="qlink" style="top:257px">About</div>
  <div class="qlink" style="top:294px">Order Now</div>
  <div class="qlink" style="top:331px">Contact</div>
  <h4 style="left:831px">Contact Informations</h4>
  <svg class="abs" style="left:848px;top:140px" width="20" height="28" viewBox="0 0 20 28"><path d="M10 27C4 19 1 14 1 10a9 9 0 0118 0c0 4-3 9-9 17z" fill="none" stroke="#fff" stroke-width="2.5"/><circle cx="10" cy="10" r="3.5" fill="#fff"/></svg>
  <div class="contact" style="top:136px;font-size:14px;line-height:1.7">1420 Willow Bend Road<br>Fairbanks, Alaska 99701</div>
  <svg class="abs" style="left:848px;top:228px" width="20" height="20" viewBox="0 0 24 24"><path d="M6 2l4 4-2 3c1 3 4 6 7 7l3-2 4 4-3 4C10 22 2 14 2 5z" fill="#fff"/></svg>
  <svg class="abs" style="left:848px;top:262px" width="20" height="15" viewBox="0 0 26 20"><rect x="1" y="1" width="24" height="18" fill="none" stroke="#fff" stroke-width="2"/><path d="M1 1l12 10L25 1" fill="none" stroke="#fff" stroke-width="2"/></svg>
  <svg class="abs" style="left:848px;top:290px" width="20" height="20" viewBox="0 0 20 20"><circle cx="10" cy="10" r="9" fill="#fff"/></svg>
  <svg class="abs" style="left:848px;top:320px" width="20" height="20" viewBox="0 0 20 20"><circle cx="10" cy="10" r="9" fill="#fff"/></svg>
  <div class="contact" style="top:226px">555-201-4477</div>
  <div class="contact" style="top:256px">marlosbakes.example</div>
  <div class="contact" style="top:287px">@marlosbakestortes</div>
  <div class="contact" style="top:318px">@marlos bakes</div>
</footer>
<div class="copyright">Copyright © 2022marlosbakes. All Right Reserved</div>

</body>
</html>
```